Business Card Design

Just looking for a good designs that looks good with our company logo. I'd like it to be simple and to the point. Just including contact information, our logo, and my name somewhere on the card so future clients know who they're contacting, and a couple services offered. The two images I attached are pictures of our logo. I don't care which color they they are, I just attached both images to give a reference of logo colors depending on the color of the card.
Names: Calvin Prewitt
Phone: 555-247-9061
Email: tidyturfcrew@mailvista.net
Services offered:
Mowing
Fertilization
Aeration
Bed & tree maintenance
and more.
Industry/Entity Type
Business
Contact Information for Business Card
Names: Calvin Prewitt
Phone: 555-247-9061
Look and feel

```html
<!DOCTYPE html>
<html lang="en">
<head>
<meta charset="utf-8">
<title>Tidy Turf Crew Business Card</title>
<link href="https://fonts.googleapis.com/css2?family=Montserrat:wght@400;500;700&display=swap" rel="stylesheet">
<style>
  :root{
    --bg:#d9d9d9;
    --card:#ffffff;
    --navy:#2b3146;
    --orange:#e8553e;
    --grey:#4a4a4a;
  }
  html,body{margin:0;padding:0;overflow:hidden}
  body{width:1200px;height:907px;background:var(--bg);font-family:"Montserrat",sans-serif;position:relative}
  .card{position:absolute;left:300px;width:600px;height:343px;background:var(--card);box-shadow:0 6px 18px rgba(0,0,0,.18);overflow:hidden}
  .card--back{top:92px}
  .card--front{top:472px}
  .swoosh{position:absolute;left:0;top:0;width:600px;height:343px}
  .brand{display:flex;align-items:center;gap:10px;color:var(--navy);font-weight:700;font-size:26px;letter-spacing:1px;text-transform:uppercase;white-space:nowrap}
  .brand__dot{width:22px;height:22px;border-radius:50%;background:var(--orange)}
  .card--back .brand{position:absolute;left:50%;top:100px;transform:translateX(-50%)}
  .services{position:absolute;left:0;right:0;top:148px;margin:0;padding:0;list-style:none;display:flex;justify-content:center;gap:8px;color:var(--grey);font-size:12px;font-weight:500;white-space:nowrap}
  .services li+li::before{content:"";display:inline-block;width:4px;height:4px;border-radius:50%;background:var(--orange);margin-right:8px;vertical-align:middle}
  .website{color:var(--navy);font-size:13px;font-weight:500}
  .card--back .website{position:absolute;right:28px;top:206px;color:var(--grey)}
  .card--front .brand{position:absolute;left:34px;top:70px;font-size:22px}
  .details{position:absolute;left:330px;top:58px;color:var(--grey);font-size:13px;line-height:1.45}
  .details__name{color:var(--navy);font-weight:700;font-size:17px;letter-spacing:1px;text-transform:uppercase;margin:0}
  .details__role{color:var(--orange);font-weight:500;font-size:14px;margin:0 0 12px}
  .details__address{margin:0 0 10px}
  .contact{list-style:none;margin:0 0 6px;padding:0}
  .contact li{display:flex;align-items:center;gap:8px}
  .contact svg{width:11px;height:11px;fill:var(--orange)}
  .details .website{color:var(--orange)}
</style>
</head>
<body>
  <section class="card card--back">
    <svg class="swoosh" viewBox="0 0 600 343" aria-hidden="true">
      <path d="M0,238 C160,292 390,328 600,343 L0,343 Z" fill="var(--orange)"/>
      <path d="M0,220 C160,276 390,316 600,336" fill="none" stroke="var(--navy)" stroke-width="5"/>
    </svg>
    <div class="brand"><span class="brand__dot"></span>Tidy Turf Crew</div>
    <ul class="services">
      <li>Mowing</li>
      <li>Fertilization</li>
      <li>Aeration</li>
      <li>Bed &amp; Tree Maintenance</li>
      <li>and more</li>
    </ul>
    <div class="website">www.tidyturfcrew.net</div>
  </section>

  <section class="card card--front">
    <svg class="swoosh" viewBox="0 0 600 343" aria-hidden="true">
      <path d="M0,238 C160,292 390,328 600,343 L0,343 Z" fill="var(--orange)"/>
      <path d="M0,220 C160,276 390,316 600,336" fill="none" stroke="var(--navy)" stroke-width="5"/>
    </svg>
    <div class="brand"><span class="brand__dot"></span>Tidy Turf Crew</div>
    <div class="details">
      <p class="details__name">Calvin Prewitt</p>
      <p class="details__role">Managing Director</p>
      <p class="details__address">417 Meadow Bend Lane<br>Cedar Hollow</p>
      <ul class="contact">
        <li><svg viewBox="0 0 12 12"><rect x="2" y="0" width="8" height="12" rx="1.5"/></svg>555-247-9061</li>
        <li><svg viewBox="0 0 12 12"><path d="M2 0h3l1 3-2 1.5a7 7 0 0 0 3.5 3.5L9 6l3 1v3c0 1-1 2-2 2A10 10 0 0 1 0 2c0-1 1-2 2-2z"/></svg>555-247-9062</li>
        <li><svg viewBox="0 0 12 12"><rect x="0" y="4" width="12" height="7" rx="1"/><rect x="3" y="0" width="6" height="4"/></svg>555-247-9063</li>
        <li><svg viewBox="0 0 12 12"><path d="M0 2h12v8H0z"/><path d="M0 2l6 4 6-4" fill="none" stroke="#fff" stroke-width="1.2"/></svg>tidyturfcrew@mailvista.net</li>
      </ul>
      <div class="website">www.tidyturfcrew.net</div>
    </div>
  </section>
</body>
</html>
```